Service Plan Sales Flyer

The Watchpost Depot (www.kelvamart.com) is a commercial security integrator that installs security cameras, access control, intrusion, two-way radios and perimeter security. We require a one page flyer for our service plan for new and existing customers. The price of the service plan is $299/yr and includes the following;
1. Discounted service rate of $118/hr
2. Free remote support ($85/hr without a plan)
3. Free remote training
4. Priority support

Please review our brochure attached and create a one page sales flyer with the end goal of having the client sign up for our annual service plan . The plan will automatically renew every year. Email sales@kelvamart.com.

Target Market(s)

commercial industrial clients - no residential

Industry/Entity Type

review our website at www.kelvamart.com

Colors
0054AA
0677BA
7BADD7
CADEEF
E8F1F8
EE7325
F08F49
F5BC92
FAE3D3
FDF4ED

Requirements
Must have
• call to action
Should not have
• too many colors

```html
<!DOCTYPE html>
<html lang="en">
<head>
<meta charset="utf-8">
<title>The Watchpost Depot – Service Plan Flyer</title>
<link href="https://fonts.googleapis.com/css2?family=Arimo:wght@400;700&family=Roboto+Condensed:wght@400;700&display=swap" rel="stylesheet">
<style>
  :root {
    --blue: #0054AA;
    --blue-mid: #0677BA;
    --blue-soft: #7BADD7;
    --blue-pale: #CADEEF;
    --blue-mist: #E8F1F8;
    --orange: #EE7325;
    --orange-soft: #F08F49;
    --peach: #FAE3D3;
    --ink: #1a1a1a;
    --page: #ffffff;
    --stage: #d9d9d9;
  }
  * { box-sizing: border-box; margin: 0; padding: 0; }
  html, body { width: 1200px; height: 1200px; overflow: hidden; }
  body { background: var(--stage); position: relative; font-family: "Arimo", Arial, sans-serif; }

  .flyer {
    position: absolute; left: 197px; top: 30px;
    width: 805px; height: 1140px;
    background: var(--page);
    overflow: hidden;
    box-shadow: 0 2px 10px rgba(0,0,0,.18);
  }
  .flyer__shapes { position: absolute; inset: 0; width: 100%; height: 100%; }

  .brand {
    position: absolute; right: 56px; top: 92px;
    display: flex; align-items: center; gap: 12px;
    font-family: "Roboto Condensed", "Arial Narrow", sans-serif;
    font-weight: 700; font-size: 34px; line-height: 1;
    color: var(--blue); text-transform: uppercase; letter-spacing: .5px;
  }
  .brand__square { width: 22px; height: 22px; background: var(--orange); }

  .about { position: absolute; right: 56px; top: 212px; width: 300px; text-align: right; color: var(--ink); }
  .about__title { font-weight: 700; font-size: 29px; line-height: 32px; margin-bottom: 32px; }
  .about__text { font-size: 17.5px; line-height: 23px; margin-bottom: 23px; hyphens: auto; -webkit-hyphens: auto; }

  .benefits { position: absolute; left: 73px; top: 0; list-style: none; }
  .benefits__item {
    position: absolute; left: 0; white-space: nowrap;
    font-family: "Roboto Condensed", "Arial Narrow", sans-serif;
    font-weight: 700; font-size: 27px; line-height: 32px;
    color: var(--ink); text-transform: uppercase;
  }

  .cta {
    position: absolute; left: 56px; right: 56px; top: 1024px; height: 88px;
    background: var(--blue); color: #fff;
    display: flex; align-items: center; justify-content: space-between;
    padding: 0 28px;
    font-family: "Roboto Condensed", "Arial Narrow", sans-serif;
  }
  .cta__offer { font-weight: 700; font-size: 27px; line-height: 30px; text-transform: uppercase; }
  .cta__price { color: var(--orange-soft); }
  .cta__note { display: block; font-weight: 400; font-size: 16px; line-height: 22px; text-transform: none; color: var(--blue-pale); }
  .cta__action {
    background: var(--orange); padding: 12px 18px;
    font-weight: 700; font-size: 19px; line-height: 24px; text-align: center;
  }
  .cta__email { display: block; font-weight: 400; font-size: 17px; }
</style>
</head>
<body>
<main class="flyer">
  <svg class="flyer__shapes" viewBox="0 0 805 1140">
    <defs>
      <filter id="soft-shadow" x="-20%" y="-20%" width="140%" height="150%">
        <feDropShadow dx="0" dy="4" stdDeviation="5" flood-color="#000" flood-opacity=".22"/>
      </filter>
      <linearGradient id="photo-tone" x1="0" y1="0" x2="0" y2="1">
        <stop offset="0" stop-color="#E8F1F8"/>
        <stop offset="1" stop-color="#CADEEF"/>
      </linearGradient>
      <linearGradient id="icon-tone" x1="0" y1="0" x2="0" y2="1">
        <stop offset="0" stop-color="#E8F1F8"/>
        <stop offset="1" stop-color="#7BADD7"/>
      </linearGradient>
    </defs>

    <polygon class="band-blue" points="0,0 279,0 407,593 0,472" fill="var(--blue)"/>
    <polygon class="band-orange" points="151,81 28,324 279,324" fill="var(--orange)"/>

    <polygon class="arrow-peach" points="70,1140 270,1000 520,1000 505,950 805,1075 805,1140" fill="var(--peach)"/>

    <g class="connectors" stroke="#CADEEF" stroke-width="1.5">
      <line x1="179" y1="235" x2="256" y2="242"/>
      <line x1="150" y1="290" x2="200" y2="330"/>
    </g>

    <g class="feature-circle" filter="url(#soft-shadow)">
      <circle cx="106" cy="235" r="73" fill="#fff"/>
      <circle cx="333" cy="242" r="77" fill="#fff"/>
      <circle cx="228" cy="395" r="81" fill="#fff"/>
    </g>
    <circle cx="106" cy="235" r="60" fill="url(#photo-tone)" role="img" aria-label="Computer monitor showing video management software"/>
    <circle cx="333" cy="242" r="64" fill="url(#photo-tone)" role="img" aria-label="Dome and box security cameras"/>
    <circle cx="228" cy="395" r="68" fill="url(#icon-tone)" role="img" aria-label="Blue software application buttons"/>

    <rect x="421" y="732" width="372" height="228" rx="6" fill="url(#photo-tone)" role="img" aria-label="Door, monitor with camera software, dome camera and bullet camera"/>

    <line x1="53" y1="624" x2="53" y2="945" stroke="var(--orange)" stroke-width="3"/>
    <g class="timeline-pin" fill="var(--orange)">
      <g transform="translate(53,624)"><circle r="14"/><polygon points="-14,2 0,16 -4,2"/><circle r="4" fill="#fff"/></g>
      <g transform="translate(53,743)"><circle r="14"/><polygon points="-14,2 0,16 -4,2"/><circle r="4" fill="#fff"/></g>
      <g transform="translate(53,858)"><circle r="14"/><polygon points="-14,2 0,16 -4,2"/><circle r="4" fill="#fff"/></g>
      <g transform="translate(53,945)"><circle r="14"/><polygon points="-14,2 0,16 -4,2"/><circle r="4" fill="#fff"/></g>
    </g>
  </svg>

  <div class="brand"><span class="brand__square"></span>The Watchpost Depot</div>

  <section class="about">
    <h2 class="about__title">ABOUT US</h2>
    <p class="about__text">From it's humble beginning in 1999, The Watchpost Depot Employees have worked hard to become one of Canada's most trusted commercial security integrators.</p>
    <p class="about__text">We started 20 years ago when businesses still used VCR tapes to record their terrible grainy video for the entire day. Now we are called on by the smartest clients (that's you) to install high definition camera systems, card swipe access control, alarm systems and intercoms … all accessible on their phones, tablets and PC.</p>
  </section>

  <ul class="benefits">
    <li class="benefits__item" style="top:650px">Discounted service<br>rate of $118/hr</li>
    <li class="benefits__item" style="top:768px">Free remote support<br>($85/hr without a plan)</li>
    <li class="benefits__item" style="top:884px">Free remote training</li>
    <li class="benefits__item" style="top:970px">Priority support</li>
  </ul>

  <section class="cta">
    <p class="cta__offer">Annual service plan <span class="cta__price">$299/yr</span>
      <span class="cta__note">Renews automatically every year</span></p>
    <p class="cta__action">Sign up today<span class="cta__email">sales@kelvamart.com</span></p>
  </section>
</main>
</body>
</html>
```